Kerno Solutions: searching for a flyer to trow in letterboxes for properties we are interested in

Hello ,

Introduction:
We are a company based in Luxembourg called "Kerno Solutions". We are specialized in buying properties on which we develop and build constructions before selling them.

Informations for the flyer:
We need a flyer to trow into the letter boxes of property owners letting them know that we are interested in buying their property, if they are interested they can give us a call.

The text for the flyer/letter is in the attachment called >>2020-03-11_KS_Text for flyer,letter there might be slight changes<<.

We need to look competent, professional and financially stable.

The flyer needs to be short and not over welling with information otherwise it will land in the trash.

We have decided that we don't want real pictures on the flyer, but shapes of any kind, blue prints, drawings are fine.

Format should be in DIN A4. We plan to print the flyer on both sides in two different languages, in other words the design will be the same on both sides only the text will be in a different language.

I also added our current logo and here is the design of the website that is under construction at the moment http://www.kernosolutions-example.lu/. The logo's color can be changed into a different blue or uni color (all white or all black).
Updates

Hi, First time user the howl thing started faster as expected. Furthermore, I need to catch my boss to discust the project with him and he is on a lot of meetings. Please give us a little bit more time. Thanks

Target Market(s)

Property owners

Requirements
Must have
• email, phone number, tax number (RCS), Tax number , matriculation and address.
see word file in attachment for information
Nice to have
• Our company logo, in one form or an other, you can be creative, the logo is in the attachment.
Should not have
• Real pictures

```html
<!DOCTYPE html>
<html lang="lb">
<head>
<meta charset="utf-8">
<title>Kerno Solutions – Flyer</title>
<link rel="stylesheet" href="https://fonts.googleapis.com/css2?family=Montserrat:wght@800&family=Source+Sans+3:wght@300;600;700&display=swap">
<style>
  :root {
    --navy: #05304c;
    --navy-deep: #042a44;
    --blue: #1a6a96;
    --blue-light: #1f75a3;
    --paper: #ffffff;
    --plan: #eef2f5;
    --drawing: #e6ebf0;
    --ink: #1b1b1b;
    --ink-soft: #2a2a2a;
    --rule: #4a4a4a;
  }
  * { margin: 0; padding: 0; box-sizing: border-box; }
  html, body { width: 1000px; height: 1200px; overflow: hidden; background: var(--paper); }
  .flyer { position: relative; width: 1000px; height: 1200px; overflow: hidden; }
  .floorplan-backdrop {
    position: absolute; left: 75px; top: 0; width: 850px; height: 1200px;
    background: var(--plan);
  }
  .house-frame { position: absolute; inset: 0; }
  .headline {
    position: absolute; left: 198px; top: 203px;
    font-family: "Montserrat", sans-serif; font-weight: 800;
    font-size: 50px; line-height: 56px; letter-spacing: 2.5px;
    color: var(--paper); text-transform: uppercase;
  }
  .building-drawing {
    position: absolute; left: 440px; top: 600px; width: 405px; height: 242px;
    background: linear-gradient(160deg, rgba(224,231,238,0.9), rgba(244,246,248,0.4));
  }
  .letter {
    position: absolute; left: 197px; top: 439px; width: 600px;
    font-family: "Source Sans 3", sans-serif; font-weight: 300;
    font-size: 17.3px; line-height: 21px; color: var(--ink-soft);
  }
  .letter p { margin-bottom: 22px; }
  .letter .salutation { font-weight: 700; font-size: 17.5px; color: var(--ink); margin-bottom: 23px; }
  .contact-list {
    position: absolute; left: 243px; top: 928px; list-style: none;
    font-family: "Source Sans 3", sans-serif; font-weight: 300;
    font-size: 19.5px; color: var(--ink-soft);
  }
  .contact-list li { position: relative; padding-left: 32px; height: 33px; line-height: 26px; white-space: nowrap; }
  .contact-icon { position: absolute; left: 0; top: 2px; width: 22px; height: 22px; }
  .divider { position: absolute; left: 563px; top: 925px; width: 1px; height: 153px; background: var(--rule); }
  .brand { position: absolute; left: 565px; top: 925px; width: 250px; text-align: center; }
  .brand-mark { display: block; width: 64px; height: 64px; margin: 0 auto 52px; background: var(--blue); }
  .brand-name {
    font-family: "Source Sans 3", sans-serif; font-weight: 700;
    font-size: 27px; line-height: 34px; letter-spacing: 0.5px; color: var(--ink);
    text-transform: uppercase; white-space: nowrap;
  }
</style>
</head>
<body>
<main class="flyer">
  <div class="floorplan-backdrop" role="img" aria-label="Faint architectural floor plan of a house in the background"></div>

  <svg class="house-frame" width="1000" height="1200" viewBox="0 0 1000 1200" aria-hidden="true">
    <defs>
      <linearGradient id="frameGradient" x1="0" y1="0" x2="0" y2="1">
        <stop offset="0" stop-color="#1a6a96"/>
        <stop offset="0.6" stop-color="#0d4a6f"/>
        <stop offset="1" stop-color="#042a44"/>
      </linearGradient>
    </defs>
    <path class="house-outline" fill="url(#frameGradient)"
      d="M95,192 V152 L500,40 L700,95 V78 H808 V125 L905,152 V192 L885,186 V1148 Q885,1160 873,1160 H115 V186 Z"/>
    <path class="gable-panel" fill="var(--navy)" d="M155,175 L500,82 L845,175 V400 H155 Z"/>
    <g class="attic-window" fill="var(--blue)">
      <rect x="457" y="140" width="38" height="40"/>
      <rect x="505" y="140" width="38" height="40"/>
      <rect x="457" y="187" width="38" height="38"/>
      <rect x="505" y="187" width="38" height="38"/>
    </g>
    <rect class="letter-panel" x="155" y="400" width="690" height="442" fill="var(--paper)"/>
    <rect class="floor-band" x="115" y="842" width="688" height="40" fill="var(--blue)"/>
    <rect class="contact-panel" x="115" y="882" width="730" height="238" fill="var(--paper)"/>
    <polygon class="corner-accent" fill="var(--blue)" points="115,1118 205,1060 205,1100 135,1150 115,1150"/>
  </svg>

  <h1 class="headline">Dir wëllt är<br>Immobilie<br>verkafen?</h1>

  <div class="building-drawing" role="img" aria-label="Line drawing of a modern multi-level house"></div>

  <section class="letter">
    <p class="salutation">Madame, Monsieur,</p>
    <p>Dir kritt dëst Schreiwes well Är Proprietéit eis Opmierksamkeet zeréckbehalen<br>huet. Mir géinge gär mat Iech iwwert d’Méiglechkeet, datt eise Betrib se opkeeft,<br>diskutéieren.</p>
    <p>Mir versécheren Iech e séieren Entscheedungsprozess, garantéieren<br>d’Bezuelung a verrechne keng Drëttkäschten.</p>
    <p>Mir géingen eis freeën, vun Iech ze héieren, a sti ganz zu<br>Ärer Verfügung fir zousätzlech Informatiounen.</p>
    <p>Mat beschte Gréiss,</p>
    <p>D’Equipe vun Kerno Solutions</p>
  </section>

  <ul class="contact-list">
    <li>
      <svg class="contact-icon" viewBox="0 0 22 22" aria-hidden="true"><circle cx="11" cy="11" r="11" fill="var(--blue)"/><path fill="#fff" d="M7.2 5.5l1.9-.4 1.2 2.8-1.3 1c.6 1.3 1.6 2.4 2.9 3l1-1.3 2.8 1.2-.4 1.9c-.2.6-.8 1-1.4.9C9.9 14.2 7.8 12.1 7.4 7c-.1-.7.2-1.3.8-1.5z"/></svg>
      691 482 305
    </li>
    <li>
      <svg class="contact-icon" viewBox="0 0 22 22" aria-hidden="true"><circle cx="11" cy="11" r="11" fill="var(--blue)"/><path fill="#fff" d="M11 4.5a4 4 0 0 0-4 4c0 3 4 8.5 4 8.5s4-5.5 4-8.5a4 4 0 0 0-4-4zm0 5.6a1.6 1.6 0 1 1 0-3.2 1.6 1.6 0 0 1 0 3.2z"/></svg>
      17 rue des Prés,
    </li>
    <li>L-3355 Leudelange</li>
    <li>
      <svg class="contact-icon" viewBox="0 0 22 22" aria-hidden="true"><circle cx="11" cy="11" r="11" fill="var(--blue)"/><rect x="5.5" y="7" width="11" height="8" fill="#fff"/><path d="M5.5 7l5.5 4.5L16.5 7" fill="none" stroke="var(--blue)" stroke-width="1.2"/></svg>
      info@kernosolutions-example.lu
    </li>
    <li>RCS : will be added</li>
  </ul>

  <div class="divider"></div>

  <div class="brand">
    <span class="brand-mark"></span>
    <div class="brand-name">Kerno Solutions</div>
  </div>
</main>
</body>
</html>
```